Boutique Health and Fitness Personal Training Studio

I would like to have a brochure designed which provides a detailed description of the services offered in my business.
I have personal training studio, We look after people from early 20's to 90's, healthy to very unhealthy.
We conduct:
A consultation
An assessment
A personalised program
Personalised training sessions
I would like to base the design around the colours of my logo (attached) and use some of (or all of) the images and information I have also attached.
I would be happy with your own images included also.

Target Market(s)

20 to 90 year olds

Industry/Entity Type

Business

Font styles to use
Serif
Sans Serif

Colors
9bcb3c
add136
cadf82
eaf2ce

Requirements
Must have
• Colour and images of fitness.
• 8.5x14 legal
• Tri fold
• 2 folds with 3 faces back n front
Nice to have
• The feeling of wellbeing
Should not have
• This is not a gym.
• It should have the feel of a private relaxed environment

```html
<!DOCTYPE html>
<html lang="en">
<head>
<meta charset="utf-8">
<title>Willow Lane Studio – Tri-fold Brochure</title>
<link rel="stylesheet" href="https://fonts.googleapis.com/css2?family=Questrial&family=Didact+Gothic&display=swap">
<style>
  :root{
    --lime:#9bcb3c;
    --lime-bright:#add136;
    --lime-soft:#cadf82;
    --lime-pale:#eaf2ce;
    --leaf:#5f9e2e;
    --leaf-dark:#3f7f22;
    --ink:#2f3a2a;
    --paper:#ffffff;
    --stage:#ece7dc;
  }
  *{box-sizing:border-box;margin:0;padding:0}
  html,body{width:1200px;height:1200px;overflow:hidden;background:var(--stage)}
  body{position:relative;font-family:"Didact Gothic","Questrial",sans-serif;color:var(--ink)}
  .sheet{position:absolute;background:var(--paper);box-shadow:0 6px 18px rgba(0,0,0,.18);overflow:hidden}
  .inside-spread{left:150px;top:40px;width:900px;height:546px}
  .front-cover{left:450px;top:620px;width:300px;height:546px}
  .sheet svg.art{position:absolute;left:0;top:0}
  .fold{position:absolute;top:0;bottom:0;width:1px;background:rgba(0,0,0,.07)}
  .block{position:absolute;font-size:9.5px;line-height:1.45}
  .block p + p{margin-top:8px}
  .heading{display:flex;align-items:center;gap:6px;font-family:"Questrial",sans-serif;font-size:15px;font-weight:400;color:var(--leaf-dark);margin-bottom:6px}
  .block.right{text-align:right}
  .block.right .heading{justify-content:flex-end}
  .leaf-bullet{width:16px;height:7px;border-radius:50%;background:var(--leaf);transform:rotate(-18deg);flex:none}
  /* cover */
  .cover-url{position:absolute;right:14px;top:14px;font-size:7px;color:#777}
  .cover-name{position:absolute;left:22px;top:44px;font-family:"Questrial",sans-serif;font-size:21px;color:var(--leaf)}
  .cover-tagline{position:absolute;left:22px;top:78px;font-family:"Questrial",sans-serif;font-size:14px;color:var(--leaf-dark);line-height:1.2}
  .cover-sub{position:absolute;left:22px;top:116px;font-size:9px;color:#555;line-height:1.4}
  .cover-sub em{font-style:normal;color:var(--lime)}
  .cover-text{position:absolute;left:18px;right:18px;top:400px;text-align:center;color:#fff;font-size:9.5px;line-height:1.45}
  .cover-text strong{display:block;font-size:12px;margin:6px 0 4px}
</style>
</head>
<body>

<section class="sheet inside-spread">
  <svg class="art" width="900" height="546" viewBox="0 0 900 546">
    <defs>
      <linearGradient id="g-class" x1="0" y1="0" x2="1" y2="1"><stop offset="0" stop-color="#bcd3e6"/><stop offset=".6" stop-color="#e9dcd0"/><stop offset="1" stop-color="#c8b3a5"/></linearGradient>
      <linearGradient id="g-tape" x1="0" y1="0" x2="1" y2="1"><stop offset="0" stop-color="#e6b08e"/><stop offset=".5" stop-color="#c9602f"/><stop offset="1" stop-color="#a8221c"/></linearGradient>
      <linearGradient id="g-food" x1="0" y1="0" x2="1" y2="1"><stop offset="0" stop-color="#8a7458"/><stop offset=".4" stop-color="#5f8c3a"/><stop offset=".7" stop-color="#e8d8c8"/><stop offset="1" stop-color="#f2eee9"/></linearGradient>
      <linearGradient id="g-gym" x1="0" y1="0" x2="1" y2="1"><stop offset="0" stop-color="#dfe7ee"/><stop offset="1" stop-color="#8aa0b2"/></linearGradient>
      <linearGradient id="g-silhouette" x1="0" y1="0" x2="0" y2="1"><stop offset="0" stop-color="#eaf2ce"/><stop offset="1" stop-color="#3a3f36"/></linearGradient>
      <clipPath id="below-wave">
        <path d="M0,405 C100,440 220,455 300,456 C420,460 520,470 600,470 C700,470 800,460 900,448 V546 H0Z"/>
      </clipPath>
    </defs>

    <!-- lower pale field -->
    <path d="M0,405 C100,440 220,455 300,456 C420,460 520,470 600,470 C700,470 800,460 900,448 V546 H0Z" fill="var(--lime-pale)"/>
    <g clip-path="url(#below-wave)">
      <rect role="img" aria-label="Silhouettes of people exercising on balance balls" x="130" y="400" width="170" height="146" fill="url(#g-silhouette)" opacity=".85"/>
      <rect role="img" aria-label="Silhouettes of people stretching and lunging" x="380" y="440" width="220" height="106" fill="url(#g-silhouette)" opacity=".85"/>
      <rect role="img" aria-label="Silhouettes of athletes training together" x="640" y="440" width="260" height="106" fill="url(#g-silhouette)" opacity=".85"/>
    </g>
    <path d="M0,405 C100,440 220,455 300,456 C420,460 520,470 600,470 C700,470 800,460 900,448" fill="none" stroke="var(--lime)" stroke-width="5"/>

    <!-- top photo band -->
    <path role="img" aria-label="Women exercising with hand weights in a bright studio" d="M0,0 H300 V125 C220,150 120,150 0,105Z" fill="url(#g-class)"/>
    <path role="img" aria-label="Hands measuring a waist with a tape measure" d="M300,0 H600 V150 C500,165 400,140 300,125Z" fill="url(#g-tape)"/>
    <path role="img" aria-label="Fresh vegetables, dumbbells and a woman stretching" d="M600,0 H900 V140 C800,150 700,180 600,210Z" fill="url(#g-food)"/>
    <path d="M0,105 C120,150 220,150 300,125 C400,140 500,165 600,150 L600,210 C700,180 800,150 900,140" fill="none" stroke="var(--lime-soft)" stroke-width="6"/>

    <!-- circle photo -->
    <circle cx="390" cy="142" r="48" fill="url(#g-gym)" stroke="var(--lime)" stroke-width="4" role="img" aria-label="Client walking on a treadmill"/>
  </svg>

  <span class="fold" style="left:300px"></span>
  <span class="fold" style="left:600px"></span>

  <div class="block" style="left:26px;top:200px;width:240px">
    <h2 class="heading"><span class="leaf-bullet"></span>What to Expect</h2>
    <p>On arrival at the studio you will be asked to complete a questionnaire, which will provide us with information regarding your background with health and fitness, as well as your goals and objectives.</p>
    <p>Please bring any relevant medical information from medical practitioners or health professionals that you feel may impact on your program.</p>
  </div>

  <div class="block right" style="left:325px;top:200px;width:250px">
    <h2 class="heading"><span class="leaf-bullet"></span>Consultation</h2>
    <p>A consultation will allow you to share your thoughts, concerns and objectives, as well as provide you with ample opportunity to expand on the answers from your questionnaire relating to your prior and current health, medical and physical concerns.</p>
  </div>

  <div class="block" style="left:322px;top:305px;width:255px">
    <h2 class="heading"><span class="leaf-bullet"></span>Assessment</h2>
    <p>An assessment will be conducted to provide us both with a baseline measure of your cardiovascular fitness, strength, flexibility, balance and body composition measures. These measures provide us with a reference for program design and also to indicate improvements along the way.</p>
  </div>

  <div class="block" style="left:622px;top:218px;width:258px">
    <h2 class="heading"><span class="leaf-bullet"></span>The program</h2>
    <p>Your program will be designed with consideration to your health and fitness background, your objectives and your strengths and weaknesses. It will be personally tailored to your needs and provide you with a plan to focus your energies on.</p>
  </div>

  <div class="block" style="left:622px;top:308px;width:258px">
    <h2 class="heading"><span class="leaf-bullet"></span>Nutrition</h2>
    <p>Nutrition is central to an effective program, as it will provide you with maximal energy for exercise as well as keeping yourself lean and healthy for a long term fitter lifestyle.</p>
    <p>Willow Lane Studio provides initial monitoring and ongoing modification in accordance with your needs.</p>
  </div>
</section>

<section class="sheet front-cover">
  <svg class="art" width="300" height="546" viewBox="0 0 300 546">
    <defs>
      <linearGradient id="g-coach" x1="0" y1="0" x2="1" y2="1"><stop offset="0" stop-color="#f1f1ef"/><stop offset=".55" stop-color="#c9ccc8"/><stop offset=".8" stop-color="#c9282a"/><stop offset="1" stop-color="#3c3c3c"/></linearGradient>
      <linearGradient id="g-cover-green" x1="0" y1="0" x2="0" y2="1"><stop offset="0" stop-color="#6aa834"/><stop offset="1" stop-color="#4e8f2a"/></linearGradient>
    </defs>
    <path role="img" aria-label="Trainer guiding a client through a stretch in the studio" d="M0,170 C100,160 200,165 300,150 V380 H0Z" fill="url(#g-coach)"/>
    <path d="M0,170 C100,160 200,165 300,150" fill="none" stroke="var(--lime)" stroke-width="5"/>
    <path d="M0,385 C120,370 220,320 300,290 V546 H0Z" fill="url(#g-cover-green)"/>
    <path d="M0,385 C120,370 220,320 300,290" fill="none" stroke="var(--lime-soft)" stroke-width="5"/>
  </svg>
  <div class="cover-url">www.willowlanestudio.com.au</div>
  <div class="cover-name">Willow Lane Studio</div>
  <div class="cover-tagline">Care in Fitness<br>&amp; Health</div>
  <div class="cover-sub">For all levels of health<br><em>and age groups.</em></div>
  <div class="cover-text">
    Experience in managing a wide range of chronic health conditions.
    <strong>Experienced professionals caring for your wellbeing</strong>
    Exercise Physiologist with over 25 years of experience managing the health and fitness needs of the community.
  </div>
</section>

</body>
</html>
```